Revamp Current Website From 2012 TO 2018

We need a ravamp to our current website. I prefer a professional corporate modern feel to it.

My Current Website is www.brightlanepromoworks.biz. Please redesign the homepage and the /certs page first....see attached document for specific instructions..

There is a lot of content at the bottom but maybe we can shorten that by using titles and a pop up of the details or something so it doesnt take too mcuh space...or maybe a red more hyperlink to see the rest of info in pop up or something or new page...

Target Market(s)

B2B, business owners, website owners, marketing companies.

Industry/Entity Type

Promotional Product

Number of Pages Required

2 page

Colors

Designer to choose colors to be used in the design.

Requirements
Must have
• Please keep in mind logo mock up I am working on that looks beautiful on dark background for header...see attached for logo
• Must use existing content I hope your marketing mind comes in to play when designing the website.
• Must have all my content provided on each page...
Nice to have
• similiar color scheme...
Should not have
• I dont like using templates because usually hard to expand on design in future so Prefer full custom designs
• Please no templates

```html
<!DOCTYPE html>
<html lang="en">
<head>
<meta charset="utf-8">
<title>Brightlane Promo Works</title>
<link href="https://fonts.googleapis.com/css2?family=Roboto:wght@300;400;500;700&display=swap" rel="stylesheet">
<style>
:root{
  --blue:#0b4d9c;
  --blue-deep:#084283;
  --blue-bright:#1e6fd0;
  --ink:#222;
  --muted:#7a7a7a;
  --soft:#f4f5f7;
  --head:#1b1b1b;
  --foot:#2a2a2a;
  --white:#fff;
}
*{box-sizing:border-box;margin:0;padding:0}
html,body{width:1200px;height:3422px;overflow:hidden}
body{font-family:"Roboto",Arial,sans-serif;color:var(--ink);background:var(--white);position:relative}
section,header,nav,footer{position:absolute;left:0;width:1200px}
.top-bar{top:0;height:98px;background:var(--head)}
.brand{position:absolute;left:84px;top:30px;display:flex;align-items:center;gap:12px;color:#3c8ee6;font-size:22px;font-weight:700;letter-spacing:.5px}
.brand-mark{width:36px;height:36px;background:#3c8ee6;border-radius:4px}
.call{position:absolute;right:84px;top:26px;display:flex;align-items:center;gap:16px;color:#fff;font-size:22px;font-weight:500}
.call-icon{width:46px;height:46px;border:2px solid #3c8ee6;border-radius:50%;display:flex;align-items:center;justify-content:center}
.main-nav{top:98px;height:50px;background:var(--blue);display:flex;justify-content:center;align-items:center;gap:54px;color:#fff;font-size:13px;font-weight:500}
.hero{top:148px;height:507px;background:linear-gradient(135deg,#d9d4cc,#efece6 45%,#c9c2b6)}
.hero-panel{position:absolute;left:141px;top:57px;width:374px;height:388px;background:rgba(80,80,80,.72);border-left:5px solid var(--blue-bright);padding:34px 30px;color:#fff}
.hero-panel h1{font-size:20px;font-weight:500;margin-bottom:22px}
.hero-panel li{list-style:none;font-size:12px;line-height:37.5px;display:flex;align-items:center;gap:18px}
.hero-panel li::before{content:"";width:9px;height:9px;border-radius:50%;border:3px solid #fff;background:transparent}
.btn{display:inline-block;background:var(--blue);color:#fff;font-weight:500;font-size:15px;text-align:center}
.hero-panel .btn{margin-top:18px;width:188px;height:42px;line-height:42px;font-size:14px}
.dots{position:absolute;left:574px;top:474px;display:flex;gap:8px}
.dots span{width:11px;height:11px;border-radius:50%;border:1px solid #aaa;background:#ddd}
.title{text-align:center;color:var(--blue);font-size:25px;font-weight:400}
.sub{text-align:center;color:var(--muted);font-size:13px;margin-top:16px}
.ways{top:655px;height:428px;background:var(--soft);padding-top:38px}
.ways .title{text-transform:uppercase}
.ways-cols{position:absolute;top:110px;left:0;width:1200px}
.way{position:absolute;width:260px;text-align:center}
.way .ico{width:110px;height:110px;border:2px solid var(--blue);border-radius:50%;margin:0 auto;display:flex;align-items:center;justify-content:center;background:#fff}
.way h3{color:var(--blue);font-size:17px;font-weight:500;margin-top:26px;line-height:24px}
.way p{color:var(--muted);font-size:12px;line-height:24px;margin-top:14px}
.video{top:1083px;height:400px}
.player{position:absolute;left:84px;top:50px;width:491px;height:299px;background:linear-gradient(135deg,#25303a,#4a6278 60%,#1b232b)}
.play{position:absolute;left:220px;top:120px;width:62px;height:44px;background:#e52d27;border-radius:10px}
.play::after{content:"";position:absolute;left:24px;top:12px;border-left:18px solid #fff;border-top:10px solid transparent;border-bottom:10px solid transparent}
.player-bar{position:absolute;left:0;bottom:0;width:100%;height:22px;background:#111}
.player-bar::before{content:"";position:absolute;left:0;top:0;width:100%;height:3px;background:#c00}
.video-copy{position:absolute;left:609px;top:66px;width:510px}
.video-copy h2{color:var(--blue);font-size:21px;font-weight:400}
.video-copy p{color:var(--muted);font-size:12px;line-height:23px;margin-top:18px}
.video-copy .btn{margin-top:30px;width:137px;height:45px;line-height:45px;font-size:14px}
.ways3{top:1483px;height:458px;background:var(--blue);color:#fff;padding-top:42px}
.ways3 h2{text-align:center;font-size:27px;font-weight:500;text-transform:uppercase}
.ways3 h3{text-align:center;font-size:22px;font-weight:300;margin-top:6px;text-transform:uppercase}
.channel{position:absolute;top:148px;width:326px}
.channel .media{height:187px;border:2px solid #fff}
.channel h4{font-size:16px;font-weight:700;margin-top:24px}
.channel p{font-size:12px;line-height:22px;margin-top:6px}
.clients{top:1941px;height:288px;padding-top:40px}
.client-row{position:absolute;top:135px;left:0;width:1200px}
.client{position:absolute;width:178px;height:102px;border:3px solid #eee;display:flex;align-items:center;justify-content:center;font-size:14px;font-weight:700;color:var(--blue)}
.testimonials{top:2229px;height:376px;background:var(--soft);padding-top:52px}
.testimonial{position:absolute;top:153px;width:330px}
.avatar{position:absolute;left:0;top:0;width:86px;height:86px;border-radius:50%;background:linear-gradient(135deg,#c9a98c,#6c5848);border:3px solid #fff}
.t-body{position:absolute;left:110px;top:0;width:220px}
.t-body p{font-size:12px;line-height:22px;color:#555}
.t-body p::before{content:"\201C";font-size:26px;color:#888;margin-right:6px;vertical-align:-6px}
.t-name{font-size:12px;font-weight:700;color:var(--blue);margin-top:14px}
.t-date{font-size:11px;color:#333;margin-top:6px}
.stars{color:#e3b21c;font-size:12px;letter-spacing:2px}
.sms{top:2605px;height:109px;background:var(--blue-deep);color:#fff}
.sms p{position:absolute;left:200px;top:44px;font-size:18px;font-weight:500}
.sms .btn-outline{position:absolute;left:869px;top:32px;width:160px;height:46px;border:2px solid #fff;text-align:center;line-height:42px;font-size:16px}
.unlimited{top:2714px;height:484px;padding-top:46px}
.unlimited h2{text-align:center;color:var(--blue);font-size:27px;font-weight:500;text-transform:uppercase}
.unlimited h3{text-align:center;color:var(--blue);font-size:22px;font-weight:300;margin-top:10px;text-transform:uppercase}
.unlimited .lead{width:1040px;margin:24px auto 0;text-align:center;color:var(--muted);font-size:12px;line-height:23px}
.feature{position:absolute;top:255px;width:330px}
.feature .ico{position:absolute;left:0;top:0;width:68px;height:68px;border-radius:50%;background:var(--blue);display:flex;align-items:center;justify-content:center}
.feature .body{position:absolute;left:80px;top:0;width:250px}
.feature h4{color:var(--blue);font-size:17px;font-weight:500}
.feature p{color:#666;font-size:12px;line-height:23px;margin-top:10px}
.feature a{display:block;margin-top:14px;color:var(--blue);font-size:12px;font-weight:700;text-decoration:underline}
.site-foot{top:3198px;height:224px;background:var(--foot);color:#fff}
.social{position:absolute;top:29px;left:0;width:1200px}
.social span{position:absolute;width:60px;height:60px;border:1px solid #bbb;border-radius:50%;display:flex;align-items:center;justify-content:center}
.foot-nav{position:absolute;top:130px;width:1200px;display:flex;justify-content:center;gap:22px;font-size:12px}
.foot-nav i{font-style:normal;color:#aaa}
.copy{position:absolute;top:172px;width:1200px;text-align:center;font-size:12px}
</style>
</head>
<body>

<header class="top-bar">
  <div class="brand"><span class="brand-mark"></span>Brightlane Promo Works</div>
  <div class="call">
    <span class="call-icon"><svg width="20" height="20" viewBox="0 0 24 24"><path d="M6.6 10.8a15 15 0 0 0 6.6 6.6l2.2-2.2a1 1 0 0 1 1-.25 11 11 0 0 0 3.6.6 1 1 0 0 1 1 1V20a1 1 0 0 1-1 1A17 17 0 0 1 3 4a1 1 0 0 1 1-1h3.5a1 1 0 0 1 1 1 11 11 0 0 0 .6 3.6 1 1 0 0 1-.25 1z" fill="#3c8ee6"/></svg></span>
    CALL US : 555-014-3827
  </div>
</header>

<nav class="main-nav">
  <span>HOME</span><span>OUR INCENTIVES</span><span>SAMPLES</span><span>HOW IT WORKS</span><span>TESTIMONIALS</span><span>FAQ</span><span>CONTACT</span><span>SIGN UP</span><span>LOG IN</span>
</nav>

<section class="hero" role="img" aria-label="Top view of a designer's desk with papers, notebooks and stationery">
  <div class="hero-panel">
    <h1>BRIGHTLANE PROMO WORKS</h1>
    <ul>
      <li>12 YEARS IN BUSINESS</li>
      <li>13,000+ CLIENTS ENROLLED</li>
      <li>2+ MILLION CERTIFICATES IN CIRCULATION</li>
      <li>170,000 + REDEMPTIONS TO DATE</li>
      <li>A RATING FTC</li>
      <li>LICENSED SELLER OF TRAVEL TSR #4418302</li>
    </ul>
    <span class="btn">30 DAY RISK FREE TRIAL</span>
  </div>
  <div class="dots"><span></span><span></span><span></span></div>
</section>

<section class="ways">
  <h2 class="title">We plug right into your existing business model in 4 ways</h2>
  <p class="sub">Boost response rates from your existing ads by adding one extra tagline: "Call for a Free Quote and receive a Three Day</p>
  <div class="ways-cols">
    <div class="way" style="left:132px">
      <div class="ico"><svg width="50" height="50" viewBox="0 0 24 24" fill="none" stroke="#0b4d9c" stroke-width="1.8"><path d="M3 10v4h3l7 4V6L6 10z"/><path d="M16 9a4 4 0 0 1 0 6M18.5 6.5a7.5 7.5 0 0 1 0 11"/></svg></div>
      <h3>Boost Response Rates<br>To Your Existing</h3>
      <p>By adding one extra tagline: "Call for a Free Quote and receive a Three Day Two Night Hotel Stay Certificate to Las Vegas or 50 + other popular destinations.</p>
    </div>
    <div class="way" style="left:472px">
      <div class="ico"><svg width="50" height="50" viewBox="0 0 24 24" fill="#0b4d9c"><rect x="4" y="14" width="3" height="6"/><rect x="9" y="11" width="3" height="9"/><rect x="14" y="8" width="3" height="12"/><rect x="3" y="20.5" width="16" height="1.2"/><text x="9.5" y="7" font-size="7" font-family="Roboto,sans-serif" font-weight="700">$</text></svg></div>
      <h3>Get More New<br>Customers</h3>
      <p>Now that you have generated a new lead, try enticing them with an upgrade and offer them Nights Plus Airfare if they purchase today</p>
    </div>
    <div class="way" style="left:812px">
      <div class="ico"><svg width="50" height="50" viewBox="0 0 24 24" fill="#0b4d9c"><rect x="3" y="8" width="18" height="12" rx="2"/><rect x="9" y="5" width="6" height="3" fill="none" stroke="#0b4d9c" stroke-width="1.6"/><rect x="3" y="12" width="18" height="1.2" fill="#fff"/></svg></div>
      <h3>Increase Repeat &amp;<br>Referral Business</h3>
      <p>Remind past clients about your products &amp; services with a 7 Night Resort Getaway in one of over 3500 destinations around the world to motivate repeat business</p>
    </div>
  </div>
</section>

<section class="video">
  <div class="player" role="img" aria-label="Promotional video still showing a hand holding a cloud graphic">
    <span class="play"></span><span class="player-bar"></span>
  </div>
  <div class="video-copy">
    <h2>WATCH VIDEO TO SAVE 20% TODAY</h2>
    <p>We are A rated with the Fair Trade Council as well as a licensed seller of travel registered with the State Travel Registry (TSR# 4418302). We also participate in The Traveler Restitution Fund (TRF), which was created to protect consumers from unscrupulous travel companies.</p>
    <p>TRF is a program that requires travel agencies like us to hold a "Passenger Trust Account" and requires that all traveler funds that we collect must be deposited into this account.</p>
    <span class="btn">READ MORE</span>
  </div>
</section>

<section class="ways3">
  <h2>Give away unlimited incentives to your</h2>
  <h3>customers three easy ways !</h3>
  <div class="channel" style="left:84px">
    <div class="media" role="img" aria-label="Printing press rollers producing certificates" style="background:linear-gradient(135deg,#8a9096,#d3d6d8 50%,#5a6066)"></div>
    <h4>PRINT</h4>
    <p>Download PDF Certificates To Print &amp; Hand Them Out Or Mail Them To Your Customers!</p>
  </div>
  <div class="channel" style="left:438px">
    <div class="media" role="img" aria-label="Hands on a laptop keyboard with envelopes flying out of the screen" style="background:linear-gradient(135deg,#3a2a1c,#a07a52 55%,#2a1d12)"></div>
    <h4>E-MAIL</h4>
    <p>Email e-certificates to your customers individually or in bulk with just one click.</p>
  </div>
  <div class="channel" style="left:789px">
    <div class="media" role="img" aria-label="Computer monitor showing a web banner with a click to watch video button" style="background:linear-gradient(135deg,#eaf0f6,#9fb4c9 55%,#44556a)"></div>
    <h4>ONLINE AUTOMATION</h4>
    <p>Add our web banners on your website. Your customers click on the banner to get their certificate.</p>
  </div>
</section>

<section class="clients">
  <h2 class="title">OUR CLIENTS</h2>
  <p class="sub">Boost response rates from your existing ads by adding one extra tagline: "Call for a Free Quote and receive a Three Day</p>
  <div class="client-row">
    <div class="client" style="left:103px">Harborstone Realty</div>
    <div class="client" style="left:308px">ValueDen</div>
    <div class="client" style="left:511px">Korvan Motors</div>
    <div class="client" style="left:716px">SkyRelay</div>
    <div class="client" style="left:919px">Harborstone Realty</div>
  </div>
</section>

<section class="testimonials">
  <h2 class="title">OUR TESTIMONIALS</h2>
  <p class="sub">Boost response rates from your existing ads by adding one extra tagline: "Call for a Free Quote and receive a Three Day</p>
  <div class="testimonial" style="left:84px">
    <div class="avatar" role="img" aria-label="Customer portrait"></div>
    <div class="t-body">
      <p>The staff was great. The owner came to our table to welcome us and they were the perfect blend of professional and welcoming!</p>
      <div class="t-name">DANA R.</div>
      <div class="t-date">POSTED ON 25 APR 2017</div>
      <div class="stars">★★★★☆</div>
    </div>
  </div>
  <div class="testimonial" style="left:436px">
    <div class="avatar" role="img" aria-label="Customer portrait"></div>
    <div class="t-body">
      <p>We are able to try so many new places with these certificates! My fiance and I are major foodies so we get to thanks to these certificates!</p>
      <div class="t-name">AVONDALE, AZ</div>
      <div class="t-date">POSTED ON 25 APR 2017</div>
      <div class="stars">★★★★☆</div>
    </div>
  </div>
  <div class="testimonial" style="left:785px">
    <div class="avatar" role="img" aria-label="Customer portrait"></div>
    <div class="t-body">
      <p>The opportunity to use the certificate is helping the restaurants to increase the market with less cost use the certificate is helping</p>
      <div class="t-name">OWEN T.</div>
      <div class="t-date">POSTED ON 25 APR 2017</div>
      <div class="stars">★★★★☆</div>
    </div>
  </div>
</section>

<section class="sms">
  <p>SEND SMS-CERTIFICATES THROUGH TEXT MESSAGING WITH JUST ONE CLICK!</p>
  <span class="btn-outline">CLICK HERE!</span>
</section>

<section class="unlimited">
  <h2>Give away an unlimited amount of certificates to</h2>
  <h3>your customers for just $99 bucks a month.</h3>
  <p class="lead">We are A rated with the Fair Trade Council as well as a licensed seller of travel registered with the State Travel Registry (TSR# 4418302). We also participate in The Traveler Restitution Fund (TRF), which was created to protect consumers from unscrupulous travel companies. TRF is a program that requires travel agencies like us to hold a "Passenger Trust Account" and requires that all traveler funds that we collect must be deposited into this account.</p>
  <div class="feature" style="left:84px">
    <div class="ico"><svg width="30" height="30" viewBox="0 0 24 24" fill="none" stroke="#fff" stroke-width="2"><rect x="3" y="4" width="18" height="12" rx="1"/><path d="M8 20h8M12 16v4"/></svg></div>
    <div class="body">
      <h4>Online Reservation Requests</h4>
      <p>First and foremost we're a marketing company &amp; we will protect the integrity of your promotions. By using separate redemption websites keeps your customers from finding out what a great value you are getting.</p>
      <a>READ MORE</a>
    </div>
  </div>
  <div class="feature" style="left:436px">
    <div class="ico"><svg width="30" height="30" viewBox="0 0 24 24" fill="#fff"><circle cx="12" cy="8" r="4"/><path d="M4 21a8 8 0 0 1 16 0z"/></svg></div>
    <div class="body">
      <h4>Superior Member Support</h4>
      <p>We are easy to contact and we always answer our phone during business hours. We even have a 24-hour live answering service that takes our calls just to guarantee that we to be busy on the other lines.</p>
      <a>READ MORE</a>
    </div>
  </div>
  <div class="feature" style="left:789px">
    <div class="ico"><svg width="30" height="30" viewBox="0 0 24 24" fill="#fff"><path d="M22 2 2 10l7 3 3 7z"/></svg></div>
    <div class="body">
      <h4>How Do We Do It</h4>
      <p>Brightlane Promo Works Group, Inc. contracts with the world leading hotel chains and resorts to help fill their otherwise empty rooms when they need it most. We help fill properties turn into future sales</p>
      <a>READ MORE</a>
    </div>
  </div>
</section>

<footer class="site-foot">
  <div class="social">
    <span style="left:387px"><svg width="20" height="20" viewBox="0 0 24 24" fill="none" stroke="#fff" stroke-width="2"><circle cx="12" cy="12" r="9"/><path d="M3 12h18M12 3a14 14 0 0 1 0 18M12 3a14 14 0 0 0 0 18"/></svg></span>
    <span style="left:460px"><svg width="20" height="20" viewBox="0 0 24 24" fill="none" stroke="#fff" stroke-width="2"><path d="M4 5h16v11H9l-5 4z"/></svg></span>
    <span style="left:533px"><svg width="20" height="20" viewBox="0 0 24 24" fill="#fff"><circle cx="6" cy="12" r="2.5"/><circle cx="18" cy="6" r="2.5"/><circle cx="18" cy="18" r="2.5"/><path d="M6 12 18 6M6 12l12 6" stroke="#fff" stroke-width="1.6"/></svg></span>
    <span style="left:606px"><svg width="20" height="20" viewBox="0 0 24 24" fill="#fff"><path d="M12 21s-8-5-8-11a4.5 4.5 0 0 1 8-3 4.5 4.5 0 0 1 8 3c0 6-8 11-8 11z"/></svg></span>
    <span style="left:677px"><svg width="20" height="20" viewBox="0 0 24 24" fill="none" stroke="#fff" stroke-width="2"><rect x="3" y="7" width="18" height="13" rx="2"/><circle cx="12" cy="13.5" r="3.5"/><path d="M8 7l2-3h4l2 3"/></svg></span>
    <span style="left:750px"><svg width="20" height="20" viewBox="0 0 24 24" fill="none" stroke="#fff" stroke-width="2"><rect x="3" y="5" width="18" height="14" rx="1"/><path d="m3 6 9 7 9-7"/></svg></span>
  </div>
  <div class="foot-nav">
    <span>HOME</span><i>|</i><span>OUR INCENTIVES</span><i>|</i><span>SAMPLES</span><i>|</i><span>HOW IT WORKS</span><i>|</i><span>TESTIMONIALS</span><i>|</i><span>FAQ</span><i>|</i><span>CONTACT</span>
  </div>
  <div class="copy">© Copyrights 2017 Brightlane Promo Works. All Rights Reserved.</div>
</footer>

</body>
</html>
```